Business card design for new, innovative company - BluePlinth

We are a new company looking for a business card design that is fun, different and quirky. Must use corporate colour green - CMYK C:55, M:0, Y:100, K:0, and corporate colour grey - C:0, M:0, Y: 0, K:70.

We have developed the first real time data application, in which people are able to profile the data of their existing customers in order to pull out more good fit clients to direct their marketing activities at.

Industry/Entity Type

Marketing

Requirements
Must have
• Logo, name, title, telephone number, fax number, email, website, address

```html
<!DOCTYPE html>
<html lang="en">
<head>
<meta charset="utf-8">
<title>BluePlinth Business Card</title>
<link href="https://fonts.googleapis.com/css2?family=Open+Sans:wght@400;600;700;800&display=swap" rel="stylesheet">
<style>
  :root {
    --green: #5b8a26;
    --green-light: #7cc242;
    --grey: #4d4d4d;
    --card: #e4e4e4;
    --page: #eeeeec;
    --white: #ffffff;
  }
  * { margin: 0; padding: 0; box-sizing: border-box; }
  html, body {
    width: 1200px; height: 900px; overflow: hidden;
    background: var(--page);
    font-family: "Open Sans", Arial, sans-serif;
  }
  .canvas {
    position: relative; width: 1200px; height: 900px;
  }
  .card {
    position: absolute; left: 320px; width: 560px; height: 320px;
    overflow: hidden;
    box-shadow: 0 6px 18px rgba(0,0,0,0.18);
  }
  .wordmark {
    position: absolute;
    font-weight: 800; font-size: 46px; letter-spacing: -1.5px;
    color: var(--grey); line-height: 1;
  }

  /* Front */
  .card-front { top: 95px; background: var(--green); }
  .front-band {
    position: absolute; left: 44px; right: 0; top: 110px; height: 140px;
    background: var(--card);
  }
  .front-accent {
    position: absolute; left: 30px; top: 110px; width: 8px; height: 140px;
    background: var(--green-light);
  }
  .card-front .wordmark { left: 30px; top: 30px; }
  .front-web {
    position: absolute; right: 34px; bottom: 22px;
    font-size: 15px; color: var(--grey);
  }
  .front-web strong { color: var(--green); font-weight: 700; }

  /* Back */
  .card-back { top: 485px; background: var(--card); }
  .card-back .wordmark { left: 34px; top: 32px; }
  .holder-name {
    position: absolute; right: 44px; top: 138px;
    font-weight: 700; font-size: 24px; color: #2e2e2e;
  }
  .contact-band {
    position: absolute; left: 0; bottom: 28px; width: 490px; height: 112px;
    background: var(--green); color: var(--white);
  }
  .contact-accent {
    position: absolute; left: 502px; bottom: 28px; width: 20px; height: 112px;
    background: var(--green-light);
  }
  .company-address {
    position: absolute; left: 24px; top: 14px;
    font-size: 13px; line-height: 1.4;
  }
  .company-address .company { font-weight: 700; }
  .contact-lines {
    position: absolute; right: 18px; bottom: 12px; text-align: right;
    font-size: 15px; line-height: 1.4;
  }
</style>
</head>
<body>
<div class="canvas">

  <section class="card card-front" aria-label="Business card front">
    <div class="front-accent"></div>
    <div class="front-band">
      <div class="wordmark">BluePlinth</div>
      <div class="front-web">www.<strong>blueplinth</strong>.com</div>
    </div>
  </section>

  <section class="card card-back" aria-label="Business card back">
    <div class="wordmark">BluePlinth</div>
    <div class="holder-name">Jenna Colbridge</div>
    <div class="contact-band">
      <div class="company-address">
        <div class="company">Plinth Data Solutions Limited</div>
        <div>22a Fenmoor Road, Marchley</div>
        <div>Northshire, NS4 2QT</div>
      </div>
      <div class="contact-lines">
        <div>mobile : 070 5518 2946</div>
        <div>office : 012 4873 5190</div>
        <div>jenna.colbridge@plinthdata.com</div>
      </div>
    </div>
    <div class="contact-accent"></div>
  </section>

</div>
</body>
</html>
```